Velmora Biz Card 2019

New business card for Velmora Property Inspections. We are a residential home inspection company in Arizona.

Target Market(s)

Real Estate

Font styles to use
Sans Serif

Requirements
Must have
• Glen Mirewick
• Home Inspector
• Velmora Property Inspections, LLC
• 480-555-0172
• glen@velmora-llc.example

```html
<!DOCTYPE html>
<html lang="en">
<head>
<meta charset="utf-8">
<title>Velmora Property Inspections – Business Card</title>
<link rel="stylesheet" href="https://fonts.googleapis.com/css2?family=Arimo:wght@400&display=swap">
<style>
  :root {
    --page-bg: #ffffff;
    --panel-dark: #3d3d3f;
    --panel-light: #f0f0f0;
    --brand-green: #3db54a;
    --brand-grey: #6b6b6d;
    --text-dark: #3a3a3a;
  }
  html, body {
    margin: 0;
    padding: 0;
    width: 1200px;
    height: 840px;
    overflow: hidden;
    background: var(--page-bg);
  }
  .canvas {
    position: relative;
    width: 1200px;
    height: 840px;
    font-family: "Arimo", Arial, sans-serif;
  }
  .business-card {
    position: absolute;
    left: 120px;
    top: 120px;
    width: 960px;
    height: 600px;
    display: flex;
  }
  .brand-panel {
    width: 480px;
    height: 100%;
    background: var(--panel-dark);
    display: flex;
    align-items: center;
    justify-content: center;
  }
  .brand-mark {
    display: flex;
    align-items: center;
    gap: 18px;
  }
  .brand-square {
    width: 34px;
    height: 34px;
    background: var(--brand-grey);
  }
  .brand-name {
    color: var(--brand-green);
    font-size: 52px;
    font-weight: 400;
    line-height: 1;
  }
  .contact-panel {
    width: 480px;
    height: 100%;
    background: var(--panel-light);
    position: relative;
  }
  .contact-block {
    position: absolute;
    left: 32px;
    top: 136px;
    margin: 0;
  }
  .contact-block p {
    margin: 0;
    font-size: 35px;
    line-height: 40px;
    white-space: nowrap;
  }
  .person-name,
  .person-title {
    color: var(--brand-green);
  }
  .company-name {
    color: var(--text-dark);
    margin-top: 14px !important;
    line-height: 47px !important;
  }
  .phone {
    color: var(--text-dark);
    margin-top: 6px !important;
  }
  .email {
    color: var(--text-dark);
  }
</style>
</head>
<body>
  <main class="canvas">
    <section class="business-card" aria-label="Business card">
      <div class="brand-panel">
        <div class="brand-mark">
          <span class="brand-square" aria-hidden="true"></span>
          <span class="brand-name">Velmora</span>
        </div>
      </div>
      <div class="contact-panel">
        <div class="contact-block">
          <p class="person-name">Glen Mirewick</p>
          <p class="person-title">Home Inspector</p>
          <p class="company-name">Velmora Property<br>Inspections,LLC</p>
          <p class="phone">480-555-0172</p>
          <p class="email">glen@velmora-llc.example</p>
        </div>
      </div>
    </section>
  </main>
</body>
</html>
```